Upmarket building and construction company needs signage

Our building company R Brent Construction, needs signage to put up on the side of our vehicle trailers and on site fencing. We are a building company that specialises in residential construction and carpentry .

I will attach our logo and some inspirational pics for site fencing as well as what our trailer looks like .
Other details i would like on the sign are our
( email) rbrentconstruction@mailbox-example.net
(mobile ) 0493 518 264
(website ) rbrentconstruction. example.net

Target Market(s)

Home owners looking for a reliable local builder who produces good quality work. I have attached some inspirational pics.

Industry/Entity Type

Building and Construction

Colors

Designer to choose colors to be used in the design.

Requirements
Must have
• Our logo, contact information
Nice to have
• We would like the design to have elements of being Elegant, Serious, Modern, Professional, Masculine, Conservative and Upmarket.

```html
<!DOCTYPE html>
<html lang="en">
<head>
<meta charset="utf-8">
<title>R Brent Construction – Site Fence Banner</title>
<link rel="stylesheet" href="https://fonts.googleapis.com/css2?family=Jost:wght@300&display=swap">
<style>
  :root {
    --banner-navy: #0b2139;
    --text-grey: #8c8f92;
    --divider-grey: #6f757c;
  }
  html, body {
    margin: 0;
    padding: 0;
    width: 1200px;
    height: 665px;
    overflow: hidden;
    background: var(--banner-navy);
  }
  .banner {
    position: relative;
    width: 1200px;
    height: 665px;
    background: var(--banner-navy);
    font-family: "Jost", "Futura", sans-serif;
    font-weight: 300;
    color: var(--text-grey);
  }
  .brand {
    position: absolute;
    left: 82px;
    top: 290px;
    width: 430px;
    text-transform: uppercase;
    font-weight: 300;
    color: var(--text-grey);
  }
  .brand-name {
    margin: 0;
    font-weight: 300;
    line-height: 1;
  }
  .brand-name .line-main {
    display: block;
    font-size: 100px;
    letter-spacing: 0.02em;
  }
  .brand-name .line-sub {
    display: block;
    margin-top: 12px;
    font-size: 46px;
    letter-spacing: 0.055em;
  }
  .brand-tagline {
    margin: 14px 0 0;
    font-size: 26px;
    letter-spacing: 0.09em;
    font-weight: 300;
  }
  .divider {
    position: absolute;
    left: 595px;
    top: 55px;
    width: 2px;
    height: 550px;
    background: var(--divider-grey);
  }
  .contact {
    position: absolute;
    right: 81px;
    top: 262px;
    text-align: right;
    font-style: normal;
  }
  .contact-email,
  .contact-phone,
  .contact-web {
    display: block;
    color: var(--text-grey);
    text-decoration: none;
  }
  .contact-email {
    font-size: 25px;
    letter-spacing: 0.01em;
  }
  .contact-phone {
    margin-top: 18px;
    font-size: 54px;
    letter-spacing: 0.03em;
    line-height: 1.1;
  }
  .contact-web {
    margin-top: 16px;
    font-size: 30px;
    letter-spacing: 0.01em;
  }
</style>
</head>
<body>
  <main class="banner">
    <section class="brand">
      <h1 class="brand-name">
        <span class="line-main">R Brent</span>
        <span class="line-sub">Construction</span>
      </h1>
      <p class="brand-tagline">Building and Carpentry</p>
    </section>

    <div class="divider" aria-hidden="true"></div>

    <address class="contact">
      <span class="contact-email">rbrentconstruction@mailbox-example.net</span>
      <span class="contact-phone">0493 518 264</span>
      <span class="contact-web">rbrentconstruction. example.net</span>
    </address>
  </main>
</body>
</html>
```